Pizza box design for 12,14,16,18 and 20 inch pizza boxes

Hello, i need a pizza box design for various size pizza boxes (12,14,16,18 and 20 inches), please review website to get an idea for design

Design should include pizzeria logo, website and store locations and phone numbers
attached is the pizzeria logo

website: www.Brellocrustnv.com
Stores:
Cedar Bend 972-418-3061
Millbrook 214-736-2193
Harlow Park 682-140-8826

Industry/Entity Type

Pizzeria Restaurant

Colors

Designer to choose colors to be used in the design.

```html
<!DOCTYPE html>
<html lang="en">
<head>
<meta charset="utf-8">
<title>Brello Crust – Pizza Box</title>
<link href="https://fonts.googleapis.com/css2?family=Share+Tech&display=swap" rel="stylesheet">
<style>
  :root {
    --backdrop: #e3e3e3;
    --board: #f7f7f5;
    --ink: #3b2b24;
    --rule: #3b2b24;
    --pill-text: #f7f7f5;
  }
  * { box-sizing: border-box; margin: 0; padding: 0; }
  html, body {
    width: 1200px; height: 900px; overflow: hidden;
    background: var(--backdrop);
    font-family: "Share Tech", sans-serif;
    color: var(--ink);
  }
  .lid {
    position: absolute; left: 220px; top: 50px;
    width: 760px; height: 620px;
    background: var(--board);
  }
  .brand {
    position: absolute; left: 0; right: 0; top: 150px;
    display: flex; align-items: center; justify-content: center; gap: 26px;
  }
  .brand-mark {
    width: 110px; height: 110px; border-radius: 50%;
    border: 5px solid var(--ink);
  }
  .brand-name {
    font-size: 64px; letter-spacing: 3px; text-transform: uppercase;
    color: var(--ink);
  }
  .menu-grid { position: absolute; left: 0; top: 0; width: 760px; height: 620px; }
  .menu-cell {
    position: absolute; text-align: center;
    font-size: 21px; letter-spacing: 2px; line-height: 1.45;
  }
  .cell-starters { left: 0; width: 250px; top: 500px; }
  .cell-mains { left: 250px; width: 260px; top: 430px; }
  .cell-extras { left: 510px; width: 250px; top: 360px; }
  .front-panel {
    position: absolute; left: 220px; top: 690px;
    width: 760px; height: 140px;
    background: var(--board);
    display: flex; align-items: center; padding: 0 24px;
  }
  .panel-name {
    font-size: 34px; letter-spacing: 2px; text-transform: uppercase;
    width: 236px; white-space: nowrap;
  }
  .stores { flex: 1; position: relative; height: 100px; }
  .store-list { display: flex; height: 62px; }
  .store {
    flex: 1; text-align: center; font-size: 19px; letter-spacing: 1.5px; line-height: 1.4;
    border-left: 2px solid var(--rule); padding-top: 4px; white-space: nowrap;
  }
  .web-pill {
    position: absolute; right: 0; bottom: 4px; width: 330px; height: 26px;
    border-radius: 13px; background: var(--ink); color: var(--pill-text);
    font-size: 15px; letter-spacing: 2px; text-align: center; line-height: 26px;
  }
</style>
</head>
<body>
  <section class="lid">
    <div class="brand">
      <span class="brand-mark"></span>
      <span class="brand-name">Brello Crust</span>
    </div>
    <svg class="menu-grid" viewBox="0 0 760 620">
      <g fill="none" stroke="#3b2b24" stroke-width="2">
        <line x1="0" y1="580" x2="760" y2="580"/>
        <polyline points="0,490 250,490 250,420 510,420 510,350 760,350"/>
        <line x1="250" y1="490" x2="250" y2="580"/>
        <line x1="510" y1="420" x2="510" y2="580"/>
      </g>
    </svg>
    <div class="menu-cell cell-starters">Appetizers<br>Calzones &amp; Stromboli</div>
    <div class="menu-cell cell-mains">Pizzas | Subs<br>Salads | Pastas</div>
    <div class="menu-cell cell-extras">Sides | Kids Menu<br>Desserts | Drinks</div>
  </section>

  <section class="front-panel">
    <div class="panel-name">Brello Crust</div>
    <div class="stores">
      <div class="store-list">
        <div class="store">Cedar Bend<br>972-418-3061</div>
        <div class="store">Millbrook<br>214-736-2193</div>
        <div class="store">Harlow Park<br>682-140-8826</div>
      </div>
      <div class="web-pill">www.Brellocrustnv.com</div>
    </div>
  </section>
</body>
</html>
```